Press On Hair Box Packaging

Details for my new Packaging Design Project will be added soon. I added some packaging concepts that I like of other companies to give you a guide.

Target Market(s)

Women ages 18-35

Font styles to use
Script

Colors
e567a6
fbd4d5
eea4c8
ed9dc4
d0ebe7
86cfc6

Requirements
Must have
• Logo Lumara Naturals Words extension kit, on the front of the box.
• Must have a clear opening in the front so the customer can see the hair.
• Instructions and photos of the girls on the back or sides of the box. Needs to say Curl it, Clip it, Crimp it! on the box.
Nice to have
• Other fun stuff to say could be: Adds instant volume and length. Beauty Essentials.

```html
<!DOCTYPE html>
<html lang="en">
<head>
<meta charset="utf-8">
<title>Lushlocks Extension Kit – Box Front</title>
<link rel="stylesheet" href="https://fonts.googleapis.com/css2?family=Codystar:wght@400&family=Poppins:wght@800&display=swap">
<style>
  :root {
    --pink-hot: #e567a6;
    --pink-bright: #f25fc0;
    --pink-soft: #fbd4d5;
    --pink-mid: #eea4c8;
    --pink-frame: #f57fcf;
    --window-grey: #b3bcba;
    --silver-light: #f4f4f4;
    --silver-mid: #c9c9c9;
    --silver-dark: #8d8d8d;
    --line-grey: #b8b8b8;
    --white: #ffffff;
    --hair-dark: #4a2f22;
    --hair-light: #8a5a3c;
  }
  html, body {
    margin: 0;
    padding: 0;
    width: 863px;
    height: 1200px;
    overflow: hidden;
    background: var(--white);
  }
  .box-front {
    position: relative;
    width: 863px;
    height: 1200px;
    overflow: hidden;
    background:
      linear-gradient(135deg, var(--pink-mid) 0%, var(--pink-soft) 22%, rgba(255,255,255,0) 42%),
      linear-gradient(315deg, var(--pink-mid) 0%, var(--pink-soft) 18%, rgba(255,255,255,0) 38%),
      var(--white);
    font-family: "Codystar", "Poppins", sans-serif;
  }
  .die-line {
    position: absolute;
    background: var(--line-grey);
  }
  .die-line--top { left: 0; top: 46px; width: 432px; height: 1px; }
  .die-line--top-2 { left: 24px; top: 56px; width: 408px; height: 1px; }
  .die-line--fold {
    left: 412px; top: 0; width: 0; height: 594px;
    border-left: 1px dashed var(--silver-dark);
    background: none;
  }
  .hang-hole {
    position: absolute;
    left: 413px; top: 59px;
    width: 34px; height: 34px;
    border-radius: 50%;
    background: var(--silver-mid);
  }
  .brand-name {
    position: absolute;
    left: 0; right: 0; top: 104px;
    margin: 0;
    text-align: center;
    font-family: "Poppins", sans-serif;
    font-weight: 800;
    font-size: 98px;
    line-height: 1;
    letter-spacing: 6px;
    color: var(--pink-bright);
  }
  .product-line {
    position: absolute;
    left: 0; right: 0; top: 244px;
    margin: 0;
    text-align: center;
    font-family: "Codystar", sans-serif;
    font-weight: 400;
    font-size: 74px;
    line-height: 1;
    letter-spacing: 2px;
    color: var(--pink-bright);
  }
  .window-frame {
    position: absolute;
    left: 120px; top: 382px;
    width: 618px; height: 650px;
    background: var(--pink-frame);
  }
  .window-opening {
    position: absolute;
    left: 30px; top: 26px;
    width: 558px; height: 600px;
    background: var(--window-grey);
  }
  .badge {
    position: absolute;
    border-radius: 50%;
    background: radial-gradient(circle at 35% 30%, var(--silver-light), var(--silver-mid) 55%, var(--silver-dark) 100%);
    box-shadow: 0 2px 6px rgba(0,0,0,0.25);
  }
  .badge__inner {
    position: absolute;
    inset: 12px;
    border-radius: 50%;
    border: 7px solid var(--pink-bright);
    background: var(--pink-bright);
    display: flex;
    flex-direction: column;
    align-items: center;
    justify-content: center;
    text-align: center;
    color: var(--white);
    overflow: hidden;
  }
  .badge__inner--photo {
    background: var(--white);
  }
  .badge__photo {
    width: 100%;
    height: 100%;
    border-radius: 50%;
  }
  .badge__photo--straight {
    background: linear-gradient(180deg, var(--white) 0%, #e9d8cc 35%, var(--hair-light) 60%, var(--hair-dark) 100%);
  }
  .badge__photo--wavy {
    background: radial-gradient(circle at 50% 40%, #d8b29a 0%, var(--hair-light) 40%, var(--hair-dark) 85%);
  }
  .badge--model-straight { left: 54px; top: 348px; width: 228px; height: 228px; }
  .badge--pieces { left: 594px; top: 338px; width: 216px; height: 216px; }
  .badge--length { left: 68px; top: 906px; width: 216px; height: 216px; }
  .badge--model-wavy { left: 492px; top: 792px; width: 312px; height: 312px; }
  .badge__figure {
    font-size: 76px;
    line-height: 0.95;
  }
  .badge__label {
    font-size: 30px;
    line-height: 1.05;
    margin-top: 4px;
  }
</style>
</head>
<body>
  <main class="box-front">
    <div class="die-line die-line--top"></div>
    <div class="die-line die-line--top-2"></div>
    <div class="die-line die-line--fold"></div>
    <div class="hang-hole"></div>

    <h1 class="brand-name">LUSHLOCKS</h1>
    <h2 class="product-line">EXTENSION KIT</h2>

    <div class="window-frame">
      <div class="window-opening"></div>
    </div>

    <div class="badge badge--model-straight">
      <div class="badge__inner badge__inner--photo">
        <div class="badge__photo badge__photo--straight" role="img" aria-label="Photo of a model wearing long straight brown hair extensions"></div>
      </div>
    </div>

    <div class="badge badge--pieces">
      <div class="badge__inner">
        <span class="badge__figure">7</span>
        <span class="badge__label">Pieces &amp;<br>Styles</span>
      </div>
    </div>

    <div class="badge badge--length">
      <div class="badge__inner">
        <span class="badge__figure">18"</span>
        <span class="badge__label">Long Hair</span>
      </div>
    </div>

    <div class="badge badge--model-wavy">
      <div class="badge__inner badge__inner--photo">
        <div class="badge__photo badge__photo--wavy" role="img" aria-label="Photo of a model wearing long wavy brown hair extensions"></div>
      </div>
    </div>
  </main>
</body>
</html>
```